Launching a new real estate agency in Monaco

Hello, I am opening a new real estate agency in Monaco. For the purpose of my activity, in order to be known quickly among a fierce competition I need an advertising campaign that will be broadcast in local magazines, newspapers, paper board, etc.

You will find example of pictures of Monaco on which I have the rights and my logo. You can always pick other images that I can buy if the price is reasonable for a commercial use (<200 $)

Please respect the color code.

I wish you good luck and look forward to give you my feedbacks

Reason: Only few projects posted were respecting the brief and of quality. Hoping to receive more in coming days

Target Market(s)

International high-end clientele of all ages, all genders.

Industry/Entity Type

Real Estate Agent

Font styles to use
Serif

Requirements
Must have
• 1/ My logo
• 2/ This message "Un nouveau regard sur l'immobilier" means in English a fresh look at real estate or new eyes on real-estate.
• 3/ My address: 14 rue des Orvilles, Passage Marcellin, 98 000 Monaco
• 4/ Phone number: +377.93.48.25.71
• 5/ Website: www.brunor-agency.com.
• 6/ Format: Files should be easily adjustable but I'd like a vertical display to fit easily in Magazines, Poster and billboard. So please work in high resolution !
Nice to have
• Please think about your design in accordance with the message I want to display.
Should not have
• A simple poster with a picture of Monaco that does not take into consideration the message of the advertisement, "Un nouveau regard sur l'immobilier" which means in english, new eyes on real-estate or a new look at real-estate, or new vision at real-estate.

```html
<!DOCTYPE html>
<html lang="fr">
<head>
<meta charset="utf-8">
<title>Brunor Agency — Un nouveau regard sur l'immobilier</title>
<link rel="stylesheet" href="https://fonts.googleapis.com/css2?family=Playfair+Display:wght@500&family=Montserrat:wght@700;800&display=swap">
<style>
  :root {
    --navy: #1b2840;
    --navy-mid: #2b3b55;
    --slate-blue: #33557a;
    --coral: #e2714f;
    --white: #ffffff;
    --rule: #5a6780;
  }
  * { margin: 0; padding: 0; box-sizing: border-box; }
  html, body { width: 848px; height: 1200px; overflow: hidden; background: var(--navy); }
  .poster { position: relative; width: 848px; height: 1200px; background: var(--navy); overflow: hidden; }

  .hero-photo {
    position: absolute; left: 0; top: 0; width: 848px; height: 736px;
    background: linear-gradient(180deg,
      #f6d27a 0%, #f08a3a 7%, #c4647a 11%, #9a7aa8 20%,
      #a88cb8 32%, #8a6f9a 45%, #6a4a5a 58%, #7a4a2e 70%, #5a3a26 85%, #3a2a22 100%);
  }

  .facets { position: absolute; left: 0; top: 0; width: 848px; height: 1200px; }

  .brand-plate {
    position: absolute; left: 50px; top: 674px; width: 267px; height: 62px;
    background: var(--navy);
    display: flex; align-items: center; justify-content: center; gap: 12px;
  }
  .brand-mark { width: 14px; height: 14px; background: var(--coral); }
  .brand-name {
    font-family: "Montserrat", sans-serif; font-weight: 700;
    font-size: 20px; letter-spacing: 3px; color: var(--white);
  }

  .headline {
    position: absolute; left: 52px; top: 792px;
    font-family: "Playfair Display", serif; font-weight: 500;
    font-size: 76px; line-height: 86px; color: var(--white);
    letter-spacing: 0.5px;
  }
  .headline .accent { color: var(--coral); display: block; }

  .contact {
    position: absolute; left: 50px; top: 1050px; width: 360px;
    font-family: "Montserrat", sans-serif; font-weight: 800;
    text-transform: uppercase; font-size: 12px; line-height: 18px;
    color: var(--white);
  }
  .contact-label { color: var(--coral); font-size: 12px; }
  .contact-block + .contact-block {
    border-top: 1px solid var(--rule); margin-top: 7px; padding-top: 7px;
  }
  .website {
    position: absolute; right: 56px; top: 1135px;
    font-family: "Montserrat", sans-serif; font-weight: 800;
    text-transform: uppercase; font-size: 12px; letter-spacing: 0.3px;
    color: var(--white);
  }
</style>
</head>
<body>
<main class="poster">
  <div class="hero-photo" role="img" aria-label="Aerial view of Monaco at sunset: the coastline, harbour and illuminated high-rise buildings beside the sea under an orange and violet sky"></div>

  <svg class="facets" viewBox="0 0 848 1200" aria-hidden="true">
    <polygon points="848,540 640,736 848,736" fill="#3f6388" opacity="0.45"/>
    <polygon points="510,736 848,736 848,770 690,900" fill="#2f5175" opacity="0.85"/>
    <polygon points="376,994 640,736 848,736 848,994" fill="#2c3d57" opacity="0.9"/>
    <polygon points="560,736 720,736 640,816" fill="#33567c" opacity="0.8"/>
    <polygon points="610,1075 848,838 848,1075" fill="#22324b" opacity="0.9"/>
  </svg>

  <div class="brand-plate">
    <span class="brand-mark"></span>
    <span class="brand-name">BRUNOR AGENCY</span>
  </div>

  <h1 class="headline">Un nouveau regard<span class="accent">sur l'immobilier</span></h1>

  <section class="contact">
    <div class="contact-block">
      <p class="contact-label">Address:</p>
      <p>14 rue des Orvilles, Passage Marcellin,<br>98 000 Monaco</p>
    </div>
    <div class="contact-block">
      <p class="contact-label">Phone number:</p>
      <p>+377.93.48.25.71</p>
    </div>
  </section>

  <p class="website">www.brunor-agency.com</p>
</main>
</body>
</html>
```